Simplified Double Diamond Diagram for Book

I need a simplified version of the Double Diamond Diagram for a book I am working on. I would like to represent the diagram with the following image/text:
- Two diamonds connected (as in each of the sample photos)
- Inclusion of "Diverge" "Converge" above each of the sides of the diamonds as shown in sample image 1 - without elaborative text
- Inclusion of "Problem" and "Solution" in each diamond as is shown in the example image 2
- I need a color version and black/white version of the image that can be turned into a mono-color version in the book.

```html
<!DOCTYPE html>
<html lang="en">
<head>
<meta charset="utf-8">
<title>Double Diamond Diagram</title>
<link href="https://fonts.googleapis.com/css2?family=Poppins:wght@700&display=swap" rel="stylesheet">
<style>
  :root {
    --paper: #ffffff;
    --ink: #111111;
    --guide: #666666;
    --blue-deep: #1976d3;
    --blue-light: #62a6ea;
    --blue-edge: #0f4a8c;
    --green-deep: #1e8e76;
    --green-light: #20a084;
    --orange-deep: #d98a22;
    --orange-light: #f09b27;
    --orange-edge: #ea5f0b;
    --mono-fill: #cacaca;
  }
  html, body {
    margin: 0;
    padding: 0;
    width: 1200px;
    height: 1200px;
    overflow: hidden;
    background: var(--paper);
  }
  .diagram-sheet {
    display: block;
    width: 1200px;
    height: 1200px;
    font-family: "Poppins", sans-serif;
  }
  .guide-line { stroke: var(--guide); stroke-width: 3; stroke-dasharray: 10 9; fill: none; }
  .phase-label { font-family: "Poppins", sans-serif; font-size: 17px; font-weight: 700; fill: var(--ink); text-anchor: middle; letter-spacing: 0.3px; }
  .stage-label { font-family: "Poppins", sans-serif; font-size: 19px; font-weight: 700; text-anchor: middle; fill: var(--paper); }
  .joint { fill: var(--ink); }
  .outline { fill: none; stroke-width: 2.5; stroke-linejoin: miter; }

  .theme-blue .half-diverge { fill: var(--blue-deep); }
  .theme-blue .half-converge { fill: var(--blue-light); }
  .theme-blue .outline { stroke: var(--blue-edge); }

  .theme-green .half-diverge { fill: var(--green-deep); }
  .theme-green .half-converge { fill: var(--green-light); }
  .theme-green .outline { stroke: none; }

  .theme-orange .half-diverge { fill: var(--orange-deep); }
  .theme-orange .half-converge { fill: var(--orange-light); }
  .theme-orange .outline { stroke: var(--orange-edge); }

  .theme-mono .half-diverge { fill: var(--mono-fill); }
  .theme-mono .half-converge { fill: var(--paper); }
  .theme-mono .outline { stroke: var(--ink); }
  .theme-mono .stage-label { fill: var(--ink); }
</style>
</head>
<body>
<svg class="diagram-sheet" viewBox="0 0 1500 1500" xmlns="http://www.w3.org/2000/svg" role="img" aria-label="Double diamond diagrams in blue, green and black and white versions, with and without problem and solution labels">

  <!-- Row 1: blue and orange -->
  <g class="diamond theme-blue" transform="translate(219,280)">
    <line class="guide-line" x1="0" y1="-205" x2="0" y2="-157"/><line class="guide-line" x1="0" y1="157" x2="0" y2="210"/>
    <polygon class="half-diverge" points="0,-157 -157,0 0,157"/><polygon class="half-converge" points="0,-157 157,0 0,157"/>
    <polygon class="outline" points="0,-157 -157,0 0,157 157,0"/>
    <text class="phase-label" transform="translate(-94,-96) rotate(-45)" dy="6">DIVERGE</text>
    <text class="phase-label" transform="translate(98,-94) rotate(45)" dy="6">CONVERGE</text>
  </g>
  <g class="diamond theme-orange" transform="translate(536,280)">
    <line class="guide-line" x1="0" y1="-205" x2="0" y2="-157"/><line class="guide-line" x1="0" y1="157" x2="0" y2="210"/>
    <polygon class="half-diverge" points="0,-157 -157,0 0,157"/><polygon class="half-converge" points="0,-157 157,0 0,157"/>
    <polygon class="outline" points="0,-157 -157,0 0,157 157,0"/>
    <text class="phase-label" transform="translate(-94,-96) rotate(-45)" dy="6">DIVERGE</text>
    <text class="phase-label" transform="translate(98,-94) rotate(45)" dy="6">CONVERGE</text>
  </g>
  <g class="diamond theme-blue" transform="translate(953,280)">
    <line class="guide-line" x1="0" y1="-205" x2="0" y2="-157"/><line class="guide-line" x1="0" y1="157" x2="0" y2="210"/>
    <polygon class="half-diverge" points="0,-157 -157,0 0,157"/><polygon class="half-converge" points="0,-157 157,0 0,157"/>
    <polygon class="outline" points="0,-157 -157,0 0,157 157,0"/>
    <text class="phase-label" transform="translate(-94,-96) rotate(-45)" dy="6">DIVERGE</text>
    <text class="phase-label" transform="translate(98,-94) rotate(45)" dy="6">CONVERGE</text>
    <text class="stage-label" x="4" y="7">PROBLEM</text>
  </g>
  <g class="diamond theme-orange" transform="translate(1270,280)">
    <line class="guide-line" x1="0" y1="-205" x2="0" y2="-157"/><line class="guide-line" x1="0" y1="157" x2="0" y2="210"/>
    <polygon class="half-diverge" points="0,-157 -157,0 0,157"/><polygon class="half-converge" points="0,-157 157,0 0,157"/>
    <polygon class="outline" points="0,-157 -157,0 0,157 157,0"/>
    <text class="phase-label" transform="translate(-94,-96) rotate(-45)" dy="6">DIVERGE</text>
    <text class="phase-label" transform="translate(98,-94) rotate(45)" dy="6">CONVERGE</text>
    <text class="stage-label" x="-3" y="7">SOLUTION</text>
  </g>
  <g class="joints">
    <circle class="joint" cx="62" cy="280" r="5"/><circle class="joint" cx="378" cy="280" r="5.5"/><circle class="joint" cx="692" cy="280" r="5"/>
    <circle class="joint" cx="796" cy="280" r="5"/><circle class="joint" cx="1112" cy="280" r="5.5"/><circle class="joint" cx="1426" cy="280" r="5"/>
  </g>

  <!-- Row 2: green and orange -->
  <g class="diamond theme-green" transform="translate(219,743)">
    <line class="guide-line" x1="0" y1="-205" x2="0" y2="-157"/><line class="guide-line" x1="0" y1="157" x2="0" y2="210"/>
    <polygon class="half-diverge" points="0,-157 -157,0 0,157"/><polygon class="half-converge" points="0,-157 157,0 0,157"/>
    <polygon class="outline" points="0,-157 -157,0 0,157 157,0"/>
    <text class="phase-label" transform="translate(-94,-96) rotate(-45)" dy="6">DIVERGE</text>
    <text class="phase-label" transform="translate(98,-94) rotate(45)" dy="6">CONVERGE</text>
  </g>
  <g class="diamond theme-orange" transform="translate(536,743)">
    <line class="guide-line" x1="0" y1="-205" x2="0" y2="-157"/><line class="guide-line" x1="0" y1="157" x2="0" y2="210"/>
    <polygon class="half-diverge" points="0,-157 -157,0 0,157"/><polygon class="half-converge" points="0,-157 157,0 0,157"/>
    <polygon class="outline" points="0,-157 -157,0 0,157 157,0"/>
    <text class="phase-label" transform="translate(-94,-96) rotate(-45)" dy="6">DIVERGE</text>
    <text class="phase-label" transform="translate(98,-94) rotate(45)" dy="6">CONVERGE</text>
  </g>
  <g class="diamond theme-green" transform="translate(954,743)">
    <line class="guide-line" x1="0" y1="-205" x2="0" y2="-157"/><line class="guide-line" x1="0" y1="157" x2="0" y2="210"/>
    <polygon class="half-diverge" points="0,-157 -157,0 0,157"/><polygon class="half-converge" points="0,-157 157,0 0,157"/>
    <polygon class="outline" points="0,-157 -157,0 0,157 157,0"/>
    <text class="phase-label" transform="translate(-94,-96) rotate(-45)" dy="6">DIVERGE</text>
    <text class="phase-label" transform="translate(98,-94) rotate(45)" dy="6">CONVERGE</text>
    <text class="stage-label" x="2" y="7">PROBLEM</text>
  </g>
  <g class="diamond theme-orange" transform="translate(1270,743)">
    <line class="guide-line" x1="0" y1="-205" x2="0" y2="-157"/><line class="guide-line" x1="0" y1="157" x2="0" y2="210"/>
    <polygon class="half-diverge" points="0,-157 -157,0 0,157"/><polygon class="half-converge" points="0,-157 157,0 0,157"/>
    <polygon class="outline" points="0,-157 -157,0 0,157 157,0"/>
    <text class="phase-label" transform="translate(-94,-96) rotate(-45)" dy="6">DIVERGE</text>
    <text class="phase-label" transform="translate(98,-94) rotate(45)" dy="6">CONVERGE</text>
    <text class="stage-label" x="-5" y="7">SOLUTION</text>
  </g>
  <g class="joints">
    <circle class="joint" cx="63" cy="743" r="5"/><circle class="joint" cx="378" cy="743" r="5.5"/><circle class="joint" cx="692" cy="743" r="5"/>
    <circle class="joint" cx="797" cy="743" r="5"/><circle class="joint" cx="1112" cy="743" r="5.5"/><circle class="joint" cx="1426" cy="743" r="5"/>
  </g>

  <!-- Row 3: mono -->
  <g class="diamond theme-mono" transform="translate(219,1213)">
    <line class="guide-line" x1="0" y1="-205" x2="0" y2="-157"/><line class="guide-line" x1="0" y1="157" x2="0" y2="210"/>
    <polygon class="half-diverge" points="0,-157 -157,0 0,157"/><polygon class="half-converge" points="0,-157 157,0 0,157"/>
    <polygon class="outline" points="0,-157 -157,0 0,157 157,0"/>
    <text class="phase-label" transform="translate(-94,-96) rotate(-45)" dy="6">DIVERGE</text>
    <text class="phase-label" transform="translate(98,-94) rotate(45)" dy="6">CONVERGE</text>
  </g>
  <g class="diamond theme-mono" transform="translate(536,1213)">
    <line class="guide-line" x1="0" y1="-205" x2="0" y2="-157"/><line class="guide-line" x1="0" y1="157" x2="0" y2="210"/>
    <polygon class="half-diverge" points="0,-157 -157,0 0,157"/><polygon class="half-converge" points="0,-157 157,0 0,157"/>
    <polygon class="outline" points="0,-157 -157,0 0,157 157,0"/>
    <text class="phase-label" transform="translate(-94,-96) rotate(-45)" dy="6">DIVERGE</text>
    <text class="phase-label" transform="translate(98,-94) rotate(45)" dy="6">CONVERGE</text>
  </g>
  <g class="diamond theme-mono" transform="translate(954,1213)">
    <line class="guide-line" x1="0" y1="-205" x2="0" y2="-157"/><line class="guide-line" x1="0" y1="157" x2="0" y2="210"/>
    <polygon class="half-diverge" points="0,-157 -157,0 0,157"/><polygon class="half-converge" points="0,-157 157,0 0,157"/>
    <polygon class="outline" points="0,-157 -157,0 0,157 157,0"/>
    <text class="phase-label" transform="translate(-94,-96) rotate(-45)" dy="6">DIVERGE</text>
    <text class="phase-label" transform="translate(98,-94) rotate(45)" dy="6">CONVERGE</text>
    <text class="stage-label" x="4" y="7">PROBLEM</text>
  </g>
  <g class="diamond theme-mono" transform="translate(1270,1213)">
    <line class="guide-line" x1="0" y1="-205" x2="0" y2="-157"/><line class="guide-line" x1="0" y1="157" x2="0" y2="210"/>
    <polygon class="half-diverge" points="0,-157 -157,0 0,157"/><polygon class="half-converge" points="0,-157 157,0 0,157"/>
    <polygon class="outline" points="0,-157 -157,0 0,157 157,0"/>
    <text class="phase-label" transform="translate(-94,-96) rotate(-45)" dy="6">DIVERGE</text>
    <text class="phase-label" transform="translate(98,-94) rotate(45)" dy="6">CONVERGE</text>
    <text class="stage-label" x="-3" y="7">SOLUTION</text>
  </g>
  <g class="joints">
    <circle class="joint" cx="63" cy="1213" r="5"/><circle class="joint" cx="378" cy="1213" r="5.5"/><circle class="joint" cx="692" cy="1213" r="5"/>
    <circle class="joint" cx="797" cy="1213" r="5"/><circle class="joint" cx="1112" cy="1213" r="5.5"/><circle class="joint" cx="1426" cy="1213" r="5"/>
  </g>
</svg>
</body>
</html>
```